Redesign cement bags for leading cement producer in south east asia

We are from Larkfield cement and would like to redesign our bag to relaunch the product line. Our bags are made of high quality PP woven sack. We are one of the leading cement producers and we want our bags to have a Larkfield classy look on each visible side when it is loading in a truck or stacking on a pallet.

Thank you for interesting in this project. Good luck.

Project Deadline Extended Reason: Hi all, I have received requests to extend the deadline. Some of the work requires revising and some of them are still on process. To be fair, I also raise my budget to compensate the time. Thanks all for your participation. Added Sunday, July 10, 2016

Target Market(s)

Construction

Industry/Entity Type

Cement

Requirements
Must have
• You will have to design two bags for two cement grades. 52.5 is of higher grade and 42.5 is of lower grade. Both are similar in design but a distinctive colours to differentiate the two at once. Please look at Reference picture 2 for ideas.
Nice to have
• You do not have to change the original logo but the Larkfield cement word font changes are required. There are no restrictions to colours and font but please refrain from using feminine colours. Instructions on rear side of the bags are now included in the scope. Please create new layout and design new user friendly symbols.
Should not have
• Since cement is a dusty product, you need avoid some colours like black as background. The dust need to be less obvious to attract attention. Our previous base colour are shown in below.
• We want a fresh look on our bag, please do not just copy our old design and make small changes. I have attached our competitors' design, please refrain from using their design as well.
• It is recommend to do some research on cement bag sector.

```html
<!DOCTYPE html>
<html lang="en">
<head>
<meta charset="utf-8">
<title>Larkfield Cement – 42.5 Bag</title>
<link rel="stylesheet" href="https://fonts.googleapis.com/css2?family=Montserrat:wght@800;900&family=Open+Sans:wght@400;600;700;800&display=swap">
<style>
:root{
  --stripe-light:#80a07e;
  --stripe-dark:#729171;
  --ink:#231f20;
  --yellow:#fcc844;
  --white:#ffffff;
}
*{margin:0;padding:0;box-sizing:border-box}
html,body{width:1200px;height:960px;overflow:hidden;background:var(--stripe-light)}
.bag{
  position:relative;width:1200px;height:960px;overflow:hidden;
  background:repeating-linear-gradient(180deg,var(--stripe-light) 0 36px,var(--stripe-dark) 36px 72px);
  font-family:"Open Sans",Arial,sans-serif;color:var(--ink);
}
.abs{position:absolute}
.rule{position:absolute;height:5px;background:var(--yellow)}
/* front */
.grade-tag{left:62px;top:44px;width:346px;height:40px;background:var(--ink);color:var(--white);
  font-weight:800;font-size:17px;letter-spacing:1px;display:flex;align-items:center;justify-content:center;transform:rotate(180deg)}
.product-type{left:62px;width:346px;top:130px;text-align:center;font-weight:800;font-size:26px;letter-spacing:.5px}
.standard{left:62px;width:346px;top:181px;text-align:center;font-weight:700;font-size:12.5px}
.brand-square{left:150px;top:300px;width:170px;height:170px;background:var(--yellow)}
.wordmark{left:40px;width:390px;top:642px;text-align:center;font-family:"Montserrat",Arial,sans-serif;font-weight:900;
  font-size:58px;line-height:64px;letter-spacing:1px}
.origin{left:62px;width:346px;top:822px;text-align:center;font-weight:700;font-size:18px;line-height:25px}
.net-weight{left:62px;width:346px;top:896px;text-align:center;font-size:19px}
/* side gussets */
.gusset{top:0;height:960px;width:118px;background:var(--ink)}
.gusset-left{left:480px}
.gusset-right{left:1082px}
.gusset-name{position:absolute;font-family:"Montserrat",Arial,sans-serif;font-weight:900;font-size:64px;letter-spacing:3px;white-space:nowrap}
.gusset-name .accent{color:var(--yellow)}
.gusset-name .plain{color:var(--white)}
.gusset-left .gusset-name{left:59px;top:425px;transform:translate(-50%,-50%) rotate(-90deg)}
.gusset-right .gusset-name{left:59px;top:530px;transform:translate(-50%,-50%) rotate(90deg)}
.gusset-mark{position:absolute;left:0;width:118px;text-align:center;color:var(--yellow);font-weight:800;font-size:14px}
.gusset-mark .square{display:block;width:46px;height:46px;background:var(--yellow);margin:0 auto 6px}
/* back */
.back{left:600px;width:480px;top:0;height:960px}
.back-mark{position:absolute;left:0;width:480px;top:12px;text-align:center;font-weight:800;font-size:13px;line-height:14px}
.back-mark .square{display:block;width:44px;height:44px;background:var(--yellow);margin:0 auto 10px}
.heading{position:absolute;left:0;width:484px;text-align:center;font-weight:800;font-size:26px}
.back .rule{left:55px;width:375px}
.copy{position:absolute;left:68px;font-weight:700;font-size:14.5px;line-height:17px;width:370px}
.bullets{position:absolute;left:52px;list-style:none;width:400px;font-weight:700;font-size:14.5px;line-height:16px;white-space:nowrap}
.bullets li{position:relative;padding-left:17px}
.bullets li::before{content:"";position:absolute;left:0;top:4px;width:9px;height:9px;background:var(--yellow)}
.mix-table{position:absolute;left:72px;top:256px;font-weight:700;font-size:12px}
.mix-rows div{height:29px}
.mix-divider{position:absolute;left:188px;top:244px;width:4px;height:108px;background:var(--yellow)}
.mix-cols{position:absolute;left:206px;top:255px;font-weight:700;font-size:12px;word-spacing:9px}
.maker{position:absolute;left:68px;top:762px;width:380px}
.maker-title{font-weight:700;font-size:14.5px;line-height:17px}
.maker-name{font-weight:800;font-size:14.5px}
.maker-name small{font-size:9px}
.maker-details{display:flex;gap:14px;font-size:10px;line-height:12.5px;font-weight:600;margin-top:6px}
.phones{font-size:10px;line-height:12.5px;font-weight:600}
.back-tag{position:absolute;left:70px;top:905px;width:345px;height:40px;background:var(--ink);color:var(--white);
  font-weight:800;font-size:17px;letter-spacing:.5px;display:flex;align-items:center;justify-content:center}
</style>
</head>
<body>
<main class="bag">

  <section class="front">
    <div class="abs grade-tag">EXPORT QUALITY 42.5 CEMENT</div>
    <h2 class="abs product-type">PORTLAND CEMENT</h2>
    <div class="rule" style="left:62px;width:346px;top:166px"></div>
    <p class="abs standard">EN 197 - 1 (2000) , Strength Class 42.5</p>
    <div class="abs brand-square" aria-hidden="true"></div>
    <h1 class="abs wordmark">LARKFIELD<br>CEMENT</h1>
    <div class="rule" style="left:62px;width:346px;top:806px"></div>
    <p class="abs origin">Export Quality<br>Product of Myanmar</p>
    <div class="rule" style="left:62px;width:346px;top:882px"></div>
    <p class="abs net-weight">Net&nbsp; Weight 50kg</p>
  </section>

  <aside class="abs gusset gusset-left">
    <div class="gusset-name"><span class="accent">LARKFIELD</span> <span class="plain">CEMENT</span></div>
    <div class="gusset-mark" style="top:846px"><span class="square"></span>LARKFIELD</div>
  </aside>

  <section class="abs back">
    <div class="back-mark"><span class="square"></span>LARKFIELD<br>CEMENT</div>

    <h3 class="heading" style="top:105px">APPLICATIONS</h3>
    <div class="rule" style="top:138px"></div>
    <p class="copy" style="top:159px">- Suitable for general concrete products.</p>

    <h3 class="heading" style="top:191px">MIXING INSTRUCTIONS</h3>
    <div class="rule" style="top:227px"></div>
    <div class="mix-table mix-rows">
      <div>Applications</div>
      <div>Lean Concrete</div>
      <div>General Concrete</div>
    </div>
    <div class="mix-divider"></div>
    <div class="mix-cols">Cement Sand Aggregate Water</div>

    <h3 class="heading" style="top:357px">RECOMMENDATIONS</h3>
    <div class="rule" style="top:393px"></div>
    <ul class="bullets" style="top:420px">
      <li style="margin-bottom:11px">During 1-3 days of curing process , concrete<br>should be sprayed with water to avoid crack.</li>
      <li>A bag of cement should be finished within<br>1 day.&nbsp; If not, seal the bag tightly.</li>
    </ul>

    <h3 class="heading" style="top:512px">PRECAUTIONS</h3>
    <div class="rule" style="top:547px"></div>
    <ul class="bullets" style="top:565px">
      <li style="margin-bottom:11px">Lift with care</li>
      <li style="margin-bottom:15px">Wear gloves while mixing or handling dry cement</li>
      <li style="margin-bottom:15px">Wear a mask while mixing dry cement</li>
      <li style="margin-bottom:15px">Keep cement away from child’s reach.</li>
      <li>Cement should be stored under shade and away<br>from moisture with pallets being raised above<br>the ground.</li>
    </ul>

    <div class="rule" style="top:750px"></div>
    <div class="maker">
      <div class="maker-title">Manufactured and distributed by:</div>
      <div class="maker-name">HARBOURSTONE <small>CEMENT CO., LTD.</small></div>
      <div class="maker-details">
        <div>No 48, 12th Street,<br>Between 20th and 21st Streets<br>Riverside Township<br>Mandalay, Myanmar</div>
        <div>Fax: (00)0 10700,<br>Email: info@harbourstone.example<br>Website: www.harbourstone.example</div>
      </div>
      <div class="phones">Tel: (00)0 10100, (00)0 10200,&nbsp; (00)0 10300<br>&nbsp;&nbsp;&nbsp;&nbsp;&nbsp;&nbsp;&nbsp;(00)0 10400, (00)0 10500,&nbsp; (00)0 10600</div>
    </div>
    <div class="rule" style="top:883px"></div>
    <div class="back-tag">EXPORT QUALITY 42.5 CEMENT</div>
  </section>

  <aside class="abs gusset gusset-right">
    <div class="gusset-mark" style="top:36px"><span class="square"></span>LARKFIELD</div>
    <div class="gusset-name"><span class="accent">LARKFIELD</span> <span class="plain">CEMENT</span></div>
  </aside>

</main>
</body>
</html>
```